Velvor IT Services Business Card

Velvor IT Services are a Perth based IT Services company. We would like to incorporate our company logo (attached) and stick with the blue that is in that design. I would like a clean look design that isn't too busy, yet creates a lasting image that is instantly recognisable in the recipients mind.

Target Market(s)

The target audience is small/medium business owners.

Industry/Entity Type

Business

Font styles to use
Serif
Sans Serif

Colors

Designer to choose colors to be used in the design.

Requirements
Must have
• The design should include:
Business name: Velvor IT Services
Directors Name: Marcus Dredge
Phone Number: 0483 906 452
Email: support@velvorit.com.au
Website: www.velvorit.com.au

```html
<!DOCTYPE html>
<html lang="en">
<head>
<meta charset="UTF-8">
<title>Velvor IT Services – Business Card</title>
<link rel="stylesheet" href="https://fonts.googleapis.com/css2?family=Bebas+Neue&display=swap">
<style>
  :root {
    --card-bg: #0e0e0e;
    --card-swoosh: #121212;
    --blue-name: #3d8fd1;
    --blue-phone: #3686cc;
    --blue-email: #2f79c3;
    --blue-web: #2a6bb7;
  }
  html, body {
    margin: 0;
    padding: 0;
    width: 1200px;
    height: 702px;
    overflow: hidden;
    background: var(--card-bg);
  }
  .card {
    position: relative;
    width: 1200px;
    height: 702px;
    background: var(--card-bg);
    overflow: hidden;
  }
  .card__swoosh {
    position: absolute;
    inset: 0;
    width: 100%;
    height: 100%;
  }
  .contact {
    position: absolute;
    left: 0;
    right: 0;
    margin: 0;
    text-align: center;
    font-family: "Bebas Neue", "Arial Narrow", sans-serif;
    font-size: 56px;
    line-height: 1;
    letter-spacing: 0.5px;
    text-transform: uppercase;
    font-weight: 400;
  }
  .contact--name  { top: 160px; color: var(--blue-name); }
  .contact--phone { top: 271px; color: var(--blue-phone); }
  .contact--email { top: 382px; color: var(--blue-email); }
  .contact--web   { top: 493px; color: var(--blue-web); }
  .contact__at {
    font-family: "Arial Narrow", Arial, sans-serif;
    font-size: 0.55em;
    vertical-align: 0.18em;
  }
</style>
</head>
<body>
  <main class="card">
    <svg class="card__swoosh" viewBox="0 0 1200 702" aria-hidden="true">
      <path d="M0 130 C 200 170, 380 250, 620 220 C 860 190, 1060 170, 1120 330 C 1180 520, 1000 660, 600 702 L 0 702 Z" fill="var(--card-swoosh)"/>
    </svg>
    <h1 class="contact contact--name">Marcus Dredge</h1>
    <p class="contact contact--phone">0483-906-452</p>
    <p class="contact contact--email">support<span class="contact__at">@</span>velvorit.com.au</p>
    <p class="contact contact--web">www.velvorit.com.au</p>
  </main>
</body>
</html>
```